Web Design Project - Investor Services

I would like a simple and elegant web design for my company "Torvelo Management". The company will provide services to Corporate and Institutional investors for their needs with local/foreign investment vehicles. The website will have four pages to start: home, about us, services, contact.
I already chose a logo, and I will attach the source file. The color that I will most probably use for the logo will be blue, and i also like grey with a white background. For the website I would like to see light colors, maybe light green or grey, with the logo either in blue, grey or white (depeding on the background).
Target Market(s)
Investment managers and tax/legal advisors from top firms. This is the reason why I want something simple and elegant.
Industry/Entity Type
Investment
Requirements
Nice to have
- I do not want many pictures in the website, but I might include a couple of pictures of Madrid and maybe a picture of myself in the about us page (still deciding). I will attach some pictures of Madrid that I like, but feel free to search for others - i have others but i am not able to attach all of them.

```html
<!DOCTYPE html>
<html lang="en">
<head>
<meta charset="utf-8">
<title>Torvelo Management</title>
<link href="https://fonts.googleapis.com/css2?family=Roboto:wght@400;500&family=Roboto+Condensed:wght@400;500&display=swap" rel="stylesheet">
<style>
:root{
  --navy:#0b1a7a;
  --navy-dark:#061263;
  --ink:#3d3d3d;
  --heading:#5a5a5a;
  --body:#6b6b6b;
  --rule:#dedede;
  --button:#2f2f2f;
  --footer:#3a3a3a;
  --white:#ffffff;
}
*{box-sizing:border-box;margin:0;padding:0}
html,body{width:1091px;height:1200px;overflow:hidden;background:var(--white)}
body{position:relative;font-family:Arial,Helvetica,sans-serif;color:var(--body)}
.top-band{position:absolute;left:0;top:0;width:1091px;height:11px;background:var(--navy-dark)}
.brand{position:absolute;left:107px;top:44px;font-family:'Roboto',sans-serif;font-weight:400;font-size:32px;color:var(--navy);letter-spacing:.5px}
.main-nav{position:absolute;top:49px;left:554px;display:flex;font-family:'Roboto Condensed',sans-serif;font-weight:500;font-size:14.5px}
.main-nav a{display:block;height:31px;line-height:31px;color:#6a6a6a;text-decoration:none;text-transform:uppercase}
.main-nav .active{background:var(--button);color:var(--white);width:71px;text-align:center;margin-right:38px}
.main-nav .about{margin-right:56px}
.main-nav .services{margin-right:56px}
.hero{position:absolute;left:109px;top:131px;width:873px;height:384px;background:linear-gradient(180deg,#6e6a78 0%,#b48d98 28%,#e8b5b2 55%,#cfa2a4 78%,#3a3840 100%)}
.hero-shadow{position:absolute;left:130px;top:508px;width:831px;height:30px;border-radius:50%;box-shadow:0 10px 18px rgba(0,0,0,.35);z-index:-1}
.hero-arrow{position:absolute;top:159px;width:55px;height:55px;background:rgba(120,90,95,.55);display:flex;align-items:center;justify-content:center}
.hero-arrow.prev{left:15px}.hero-arrow.next{right:15px}
.feature{position:absolute;top:563px;width:277px}
.feature h2,.block h2{font-family:'Roboto Condensed',sans-serif;font-weight:500;font-size:22px;color:var(--heading);text-transform:uppercase;display:flex;align-items:center;gap:9px;height:28px}
.feature hr,.block hr{border:0;border-top:1px solid var(--rule);margin-top:12px;width:273px}
p.copy{font-size:10.4px;line-height:13.2px;text-align:justify;margin-top:19px;width:277px}
.more{display:block;width:56px;height:29px;line-height:29px;background:var(--button);color:var(--white);font-family:'Roboto Condensed',sans-serif;font-size:11.5px;text-align:center;text-decoration:none}
.feature .more{position:absolute;top:123px}
.section-rule{position:absolute;left:90px;top:748px;width:920px;height:4px;background:radial-gradient(ellipse at center,rgba(0,0,0,.18) 0%,rgba(0,0,0,0) 70%)}
.block{position:absolute;top:792px;width:277px;height:300px}
.photo{margin-top:16px;width:273px;height:124px}
.photo.city{background:linear-gradient(135deg,#8c8a88,#d2cfca 45%,#6f7a8a 70%,#3c3b3a)}
.photo.coins{background:linear-gradient(160deg,#c5c9c8,#8a6a52 40%,#b07a56 55%,#d7dbd4 85%)}
.block .copy{margin-top:20px}
.block .more{position:absolute;top:287px}
.news-nav{position:absolute;right:4px;top:6px;display:flex;gap:6px}
.news-nav span{width:13px;height:13px;background:#111;display:flex;align-items:center;justify-content:center}
.news-item{position:relative;padding-left:30px;border-bottom:1px solid var(--rule);height:76px;padding-top:14px;width:273px}
.news-item:last-of-type{border-bottom:0}
.news-item svg{position:absolute;left:0;top:16px}
.news-item h3{font-size:10.6px;font-weight:400;color:var(--navy)}
.news-item p{font-size:10.4px;line-height:13.2px;text-align:justify;margin-top:9px}
.footer{position:absolute;left:0;top:1131px;width:1091px;height:69px;background:var(--footer)}
.footer small{position:absolute;left:109px;top:31px;font-size:11px;color:#e8e8e8}
.social{position:absolute;right:106px;top:17px;display:flex;gap:7px}
.social span{width:29px;height:29px;border-radius:50%;background:#6f6f6f}
</style>
</head>
<body>
<div class="top-band"></div>
<div class="brand">Torvelo Management</div>
<nav class="main-nav">
  <a class="active" href="#">Home</a>
  <a class="about" href="#">About us</a>
  <a class="services" href="#">Services</a>
  <a href="#">Contact</a>
</nav>

<div class="hero-shadow"></div>
<div class="hero" role="img" aria-label="Photo of a city skyline with four tall towers at dusk under a pink sky">
  <div class="hero-arrow prev"><svg width="14" height="22" viewBox="0 0 14 22"><path d="M11 2 3 11l8 9" fill="none" stroke="#a07c80" stroke-width="3"/></svg></div>
  <div class="hero-arrow next"><svg width="14" height="22" viewBox="0 0 14 22"><path d="M3 2l8 9-8 9" fill="none" stroke="#a07c80" stroke-width="3"/></svg></div>
</div>

<section class="feature" style="left:109px">
  <h2><svg width="20" height="26" viewBox="0 0 20 26"><rect x="1" y="3" width="18" height="22" fill="#444"/><rect x="6" y="0" width="8" height="5" fill="#444"/><g stroke="#fff" stroke-width="1.4"><path d="M4 10h12M4 14h12M4 18h12M4 22h8"/></g></svg>Planning</h2>
  <hr>
  <p class="copy">potmnis iste natus error sit voluptatem accusantium doloremque laudantium, totam rem aperiam, eaque ipsa quae ab illo inventore veritatis et quasi architecto beatae vitae dicta sunt explicabo.</p>
  <a class="more" href="#">MORE</a>
</section>
<section class="feature" style="left:408px">
  <h2><svg width="20" height="26" viewBox="0 0 20 26"><path d="M10 1a8 8 0 0 0-5 14v4h10v-4A8 8 0 0 0 10 1z" fill="#333"/><rect x="6" y="20" width="8" height="2" fill="#333"/><rect x="7" y="23" width="6" height="2" fill="#333"/></svg>Solution</h2>
  <hr>
  <p class="copy">potmnis iste natus error sit voluptatem accusantium doloremque laudantium, totam rem aperiam, eaque ipsa quae ab illo inventore veritatis et quasi architecto beatae vitae dicta sunt explicabo.</p>
  <a class="more" href="#">MORE</a>
</section>
<section class="feature" style="left:709px">
  <h2><svg width="24" height="28" viewBox="0 0 24 28"><circle cx="12" cy="8" r="7" fill="#333"/><path d="M1 28v-5c0-4 5-7 11-7s11 3 11 7v5z" fill="#333"/></svg>Approach</h2>
  <hr>
  <p class="copy">potmnis iste natus error sit voluptatem accusantium doloremque laudantium, totam rem aperiam, eaque ipsa quae ab illo inventore veritatis et quasi architecto beatae vitae dicta sunt explicabo.</p>
  <a class="more" href="#">MORE</a>
</section>

<div class="section-rule"></div>

<section class="block" style="left:109px">
  <h2>Who we are</h2>
  <hr>
  <div class="photo city" role="img" aria-label="Photo of ornate historic city buildings along a busy avenue"></div>
  <p class="copy">potmnis iste natus error sit voluptatem accusantium doloremque laudantium, totam rem aperiam, eaque ipsa quae ab illo inventore veritatis et quasi architecto beatae vitae dicta sunt explicabo. eaque ipsa quae ab illo inventore veritatis et quasi architecto beatae vitae dicta sunt explicabo.</p>
  <a class="more" href="#">MORE</a>
</section>
<section class="block" style="left:409px">
  <h2>What we do</h2>
  <hr>
  <div class="photo coins" role="img" aria-label="Photo of stacked coins resting on banknotes"></div>
  <p class="copy">potmnis iste natus error sit voluptatem accusantium doloremque laudantium, totam rem aperiam, eaque ipsa quae ab illo inventore veritatis et quasi architecto beatae vitae dicta sunt explicabo. eaque ipsa quae ab illo inventore veritatis et quasi architecto beatae vitae dicta sunt explicabo.</p>
  <a class="more" href="#">MORE</a>
</section>
<section class="block" style="left:711px">
  <h2>Latest news</h2>
  <div class="news-nav">
    <span><svg width="6" height="8" viewBox="0 0 6 8"><path d="M5 0 1 4l4 4" fill="none" stroke="#fff" stroke-width="1.6"/></svg></span>
    <span><svg width="6" height="8" viewBox="0 0 6 8"><path d="M1 0l4 4-4 4" fill="none" stroke="#fff" stroke-width="1.6"/></svg></span>
  </div>
  <hr>
  <div class="news-item"><svg width="22" height="16" viewBox="0 0 22 16"><path d="M2 5h4l12-5v16L6 11H2z" fill="#333"/><rect x="5" y="11" width="3" height="5" fill="#333"/></svg><h3>potmnis iste natus error sit voluptatem</h3><p>accusantium doloremque laudantium, totam rem aperiam, eaque ipsa quae ab illo inventore</p></div>
  <div class="news-item"><svg width="22" height="16" viewBox="0 0 22 16"><path d="M2 5h4l12-5v16L6 11H2z" fill="#333"/><rect x="5" y="11" width="3" height="5" fill="#333"/></svg><h3>potmnis iste natus error sit voluptatem</h3><p>accusantium doloremque laudantium, totam rem aperiam, eaque ipsa quae ab illo inventore</p></div>
  <div class="news-item"><svg width="22" height="16" viewBox="0 0 22 16"><path d="M2 5h4l12-5v16L6 11H2z" fill="#333"/><rect x="5" y="11" width="3" height="5" fill="#333"/></svg><h3>potmnis iste natus error sit voluptatem</h3><p>accusantium doloremque laudantium, totam rem aperiam, eaque ipsa quae ab illo inventore</p></div>
  <a class="more" href="#">MORE</a>
</section>

<footer class="footer">
  <small>© 2013 - Torvelo Management. All Rights Reserved.</small>
  <div class="social"><span></span><span></span><span></span><span></span><span></span></div>
</footer>
</body>
</html>
```